Corvane Agribusiness Consulting needs a Website Design.

We need a website design for a new company based in UK. Corvane offers agribusiness consulting and farm design services to farmers, smallholders and the wider agribusiness industry to assist clients in adopting more sustainable and regenerative production, processing and marketing practices.
Services are offered face-to-face and on a remote platform.
Services are offered in the UK and overseas.
We would like to see designs that reflect the natural environment, business and sustainability. Desired colours; green, blue, grey. The final design should communicate professionalism in the rural economy.
The design should be able to be customized by the client to make future changes and additions.
Target Market(s)
Farmers, smallholders, and the agricultural industry in UK and overseas.
Industry/Entity Type
Agribusiness
Number of Pages Required
4 page

```html
<!DOCTYPE html>
<html lang="en">
<head>
<meta charset="utf-8">
<title>Corvane – International Agribusiness Consulting</title>
<link href="https://fonts.googleapis.com/css2?family=PT+Sans:wght@400;700&display=swap" rel="stylesheet">
<style>
:root{
  --teal:#13a68d;
  --lime:#8cc63f;
  --ink:#3a3a3a;
  --muted:#6f6f6f;
  --bar:#f3f3f3;
  --soft:#f7f7f7;
  --footer:#333333;
  --footer-deep:#292929;
  --footer-text:#9a9a9a;
}
*{box-sizing:border-box;margin:0;padding:0}
html,body{width:832px;height:1200px;overflow:hidden}
body{font-family:"PT Sans",sans-serif;color:var(--ink);background:#fff;position:relative}
.abs{position:absolute}

.topbar{top:0;left:0;width:832px;height:28px;background:var(--bar)}
.topbar .info{font-size:7px;color:var(--muted);top:9px;display:flex;align-items:center;gap:5px}
.topbar .divider{left:420px;top:0;width:1px;height:28px;background:#d4d4d4}
.search{left:584px;top:4px;width:139px;height:16px;border:1px solid #d6d6d6;background:#fff;font-size:7px;color:#888;padding:3px 8px}
.search svg{position:absolute;right:3px;top:2px}

.brand{left:106px;top:32px}
.brand-name{font-size:34px;font-weight:400;color:var(--teal);letter-spacing:1px;line-height:1}
.brand-tag{font-size:12.5px;color:#222;margin-top:3px}

.nav{top:52px;left:383px;display:flex;align-items:center;font-size:9px;color:#444}
.nav a{color:inherit;text-decoration:none}
.nav .active{background:var(--lime);color:#fff;width:61px;height:22px;display:flex;align-items:center;justify-content:center;position:relative}
.nav .active::after{content:"";position:absolute;right:0;bottom:-6px;border-left:6px solid transparent;border-top:6px solid var(--lime)}
.nav .sep{color:var(--lime);margin:0 14px}

.hero{top:98px;left:0;width:832px;height:358px;background:linear-gradient(180deg,#cfd5da 0%,#e2e5e8 35%,#b9c2c8 66%,#8fa873 76%,#86b04a 84%,#7aa83c 100%)}
.hero-copy{left:107px;top:214px}
.hero-copy h1{font-size:23px;font-weight:700;color:#3f3f3f;letter-spacing:.5px;line-height:1}
.hero-copy h2{font-size:16px;font-weight:700;color:#454545;letter-spacing:.5px;line-height:22px;margin-top:6px}
.btn-start{left:107px;top:298px;width:91px;height:30px;background:var(--teal);color:#fff;font-size:11.5px;display:flex;align-items:center;justify-content:center}

.section-title{font-size:18px;font-weight:700;color:#3a3a3a;letter-spacing:.3px;text-align:center}
.welcome-title{top:483px;left:0;width:832px}
.rule{top:493px;height:4px;width:160px;background:repeating-linear-gradient(90deg,#d9d9d9 0 1px,transparent 1px 2px);border-top:1px solid #e6e6e6;border-bottom:1px solid #e6e6e6}
.welcome-text{left:126px;top:528px;width:584px;font-size:8.4px;line-height:16px;color:var(--muted);text-align:justify;text-align-last:center;letter-spacing:.2px}
.welcome-text p+p{margin-top:16px}
.pill{background:var(--teal);color:#fff;border-radius:10px;display:flex;align-items:center;justify-content:center;font-size:7.5px}
.read-more{left:384px;top:652px;width:63px;height:18px}

.services{top:685px;left:0;width:832px;height:301px;background:var(--soft)}
.services-title{top:713px;left:0;width:832px}
.services-sub{top:741px;left:0;width:832px;text-align:center;font-size:11px;color:#7a7a7a}
.card{top:787px;width:174px;height:149px;background:#fff;border:1px solid #dedede;box-shadow:0 6px 6px -4px rgba(0,0,0,.15)}
.card .photo{position:absolute;left:5px;top:5px;width:164px;height:108px}
.card .caption{position:absolute;top:120px;left:0;width:100%;text-align:center;font-size:10.5px;color:#444;letter-spacing:.2px}
.card .pill{position:absolute;left:48px;top:141px;width:78px;height:20px;font-size:8px}

.footer{top:986px;left:0;width:832px;height:182px;background:var(--footer);border-top:2px solid var(--lime)}
.footer h3{position:absolute;font-size:14px;font-weight:700;color:#e8e8e8;letter-spacing:1.3px;top:35px}
.tweet-mark{position:absolute;left:133px;top:66px;width:20px;height:20px;border-radius:50%;background:#2aa3e6}
.tweet-text{position:absolute;left:131px;top:104px;width:170px;font-size:8px;line-height:12px;color:#8a8a8a;letter-spacing:.2px}
.tweet-link{position:absolute;left:130px;top:152px;font-size:7.5px;color:var(--lime)}
.links{position:absolute;left:371px;top:62px;width:144px;list-style:none}
.links li{font-size:8.5px;color:#9a9a9a;letter-spacing:.6px;height:16px;line-height:14px;border-bottom:1px dotted #555;padding-left:18px;position:relative}
.links li::before{content:"";position:absolute;left:3px;top:5px;border-left:3px solid #777;border-top:2px solid transparent;border-bottom:2px solid transparent}
.contact{position:absolute;left:561px;top:63px;font-size:8.5px;color:#d0d0d0;letter-spacing:.4px}
.contact .row{display:flex}
.contact .k{width:48px}
.contact .v{width:96px;font-size:7px;line-height:12px;color:#7c7c7c;letter-spacing:.3px}
.contact .v.hl{color:var(--lime);font-size:6.2px;text-transform:uppercase}
.copyright{top:1168px;left:0;width:832px;height:32px;background:var(--footer-deep);font-size:7px;color:var(--lime);text-align:center;line-height:32px;letter-spacing:.3px}
</style>
</head>
<body>

<div class="abs topbar">
  <div class="abs info" style="left:298px">
    <svg width="9" height="9" viewBox="0 0 10 10"><path d="M2 1l2 0 1 2-1 1c.5 1 1.5 2 2.5 2.5l1-1 2 1v2c-4 0-7.5-3.5-7.5-7.5z" fill="#aaa"/></svg>
    Call Us: (+44) 01632 960418
  </div>
  <div class="abs divider"></div>
  <div class="abs info" style="left:430px">
    <svg width="11" height="8" viewBox="0 0 11 8"><rect x=".5" y=".5" width="10" height="7" fill="none" stroke="#aaa"/><path d="M.5.5l5 4 5-4" fill="none" stroke="#aaa"/></svg>
    E-mail Us: : info@corvane-agri.co.uk
  </div>
  <div class="abs search">Search your Topic
    <svg width="11" height="11" viewBox="0 0 11 11"><circle cx="4.5" cy="4.5" r="3.3" fill="none" stroke="#555" stroke-width="1.3"/><path d="M7 7l3 3" stroke="#555" stroke-width="1.6"/></svg>
  </div>
</div>

<div class="abs brand">
  <div class="brand-name">Corvane</div>
  <div class="brand-tag">international agribusiness consulting</div>
</div>

<nav class="abs nav">
  <a class="active" href="#">HOME</a>
  <a href="#" style="margin-left:16px">ABOUT US</a><span class="sep">|</span>
  <a href="#">WHAT WE DO</a><span class="sep">|</span>
  <a href="#">SERVICES</a><span class="sep">|</span>
  <a href="#">CONTACT</a>
</nav>

<section class="abs hero" role="img" aria-label="Large oak tree standing in a green meadow under a cloudy sky"></section>
<div class="abs hero-copy">
  <h1>CORVANE PROVIDES</h1>
  <h2>AGRIBUSINESS CONSULTING<br>AND SOLUTIONS</h2>
</div>
<a class="abs btn-start">Get Started!</a>

<div class="abs rule" style="left:126px"></div>
<div class="abs rule" style="left:550px"></div>
<h2 class="abs section-title welcome-title">WELCOME TO CORVANE</h2>
<div class="abs welcome-text">
  <p>Martin has over 25 years professional experience working in the agricultural industry in the UK and overseas. Beginning his career with not-for-profit organisations in Asia and Africa, Martin assisted rural communities rehabilitate and develop their farm businesses and local economies with large scale sustainable agricultural programs.</p>
  <p>Martin established Corvane and continues to undertake consulting assignments in Asia, Australia and South Africa assisting commercial and government clients to adopt regenerative agriculture practices into their existing and new business and programs.</p>
</div>
<a class="abs pill read-more">read more</a>

<section class="abs services"></section>
<h2 class="abs section-title services-title">WHAT WE DO</h2>
<p class="abs services-sub">Features we are proud lorem ipsum meta data of our company</p>

<div class="abs card" style="left:121px">
  <div class="photo" role="img" aria-label="Farmer working beside a wooden fence in a green field" style="background:linear-gradient(180deg,#4f7a34 0%,#7fb23e 100%)"></div>
  <div class="caption">AGRIBUSINESS CONSULTING</div>
  <a class="pill">KNOW MORE</a>
</div>
<div class="abs card" style="left:328px">
  <div class="photo" role="img" aria-label="Herd of cattle grazing on pasture in front of trees" style="background:linear-gradient(180deg,#a9c9e4 0%,#5f8a3a 45%,#7fb43a 100%)"></div>
  <div class="caption">AGRIBUSINESS PRODUCTION</div>
  <a class="pill">KNOW MORE</a>
</div>
<div class="abs card" style="left:536px">
  <div class="photo" role="img" aria-label="Crates of fresh locally grown vegetables at a market stall" style="background:linear-gradient(135deg,#7a8a4a 0%,#c28a55 55%,#8a7a62 100%)"></div>
  <div class="caption">AGRIBUSINESS MARKETING</div>
  <a class="pill">KNOW MORE</a>
</div>

<footer class="abs footer">
  <h3 style="left:129px">LATEST TWEETS</h3>
  <div class="tweet-mark"></div>
  <p class="tweet-text">RT @fieldnotes: Integer facilisis pharetra risus eget auctor. Nullam viverra dapibus tellus, sit amet cursus turpis vulputate</p>
  <div class="tweet-link">http://co/fn48kq2</div>

  <h3 style="left:366px">IMPORTANT LINKS</h3>
  <ul class="links">
    <li>Home</li><li>About us</li><li>Consulting</li><li>Production</li><li>Marketing</li><li>Services</li>
  </ul>

  <h3 style="left:558px">CONTACT US</h3>
  <div class="contact">
    <div class="row" style="height:40px"><span class="k">Address:</span><span class="v">18-20 Millbrook Lane, Ashworth, AB1 2CD</span></div>
    <div class="row" style="height:21px"><span class="k">Phone:</span><span class="v">(+44) 01632 960418</span></div>
    <div class="row" style="height:18px"><span class="k">E-mail:</span><span class="v hl">info@corvane-agri.co.uk</span></div>
    <div class="row"><span class="k">Twitter:</span><span class="v hl">@CorvaneFarms</span></div>
  </div>
</footer>
<div class="abs copyright">© 2015 Corvane , All Rights Reserved.</div>

</body>
</html>
```